Business Card for Lorena Whitfield

Name: Lorena Whitfield
Title: Realtor
Email: Lorena@LorenaWhitfieldRE.com
Phone: 480-555-0137

On the front of the business card, I would like the photo, the contact information and the Lorena Whitfield Logo. The backside is required to have the Broker logo and the required logos. Please use the colors from the logo design. Our company has a classy, professional look.

```html
<!DOCTYPE html>
<html lang="en">
<head>
<meta charset="UTF-8">
<title>Lorena Whitfield – Business Card</title>
<link href="https://fonts.googleapis.com/css2?family=Cinzel:wght@400;600&family=Montserrat:wght@400;500&display=swap" rel="stylesheet">
<style>
  :root {
    --page-bg: #e4e4e4;
    --card-white: #ffffff;
    --brand-red: #b8192f;
    --brand-gray: #4a4a4c;
    --line-gray: #59595b;
    --text-gray: #555557;
    --back-dark: #4b4b4d;
    --emboss: #3e3e40;
    --emboss-light: #5a5a5c;
    --badge-white: #f2f2f2;
  }
  * { margin: 0; padding: 0; box-sizing: border-box; }
  html, body { width: 1200px; height: 801px; overflow: hidden; }
  body {
    background: var(--page-bg);
    display: flex;
    align-items: center;
    justify-content: center;
    gap: 40px;
    font-family: "Montserrat", Arial, sans-serif;
  }
  .card {
    position: relative;
    width: 540px;
    height: 309px;
    overflow: hidden;
    box-shadow: 0 4px 14px rgba(0,0,0,0.18);
  }
  .card-front { background: var(--card-white); }
  .front-art { position: absolute; inset: 0; }
  .brand-mark {
    position: absolute;
    left: 34px;
    top: 58px;
    display: flex;
    align-items: center;
    gap: 10px;
    font-family: "Cinzel", Georgia, serif;
    font-weight: 400;
    color: var(--brand-red);
  }
  .brand-square {
    width: 36px; height: 36px;
    background: var(--brand-red);
  }
  .brand-name { font-size: 21px; letter-spacing: 1px; line-height: 1; }
  .brand-sub { font-size: 10px; letter-spacing: 2px; margin-top: 4px; }
  .agent {
    position: absolute;
    left: 34px;
    top: 132px;
  }
  .agent-name {
    font-family: "Cinzel", Georgia, serif;
    color: var(--brand-red);
    font-size: 20px;
    letter-spacing: 0.5px;
  }
  .agent-title { color: var(--text-gray); font-size: 13px; margin-top: 2px; }
  .contact {
    position: absolute;
    left: 34px;
    top: 198px;
    list-style: none;
    font-size: 12.5px;
    color: var(--text-gray);
  }
  .contact li { display: flex; align-items: center; gap: 8px; margin-bottom: 5px; }
  .contact svg { width: 12px; height: 12px; fill: var(--brand-red); }

  .card-back { background: var(--back-dark); }
  .crest-ornament {
    position: absolute;
    left: 170px; top: 38px;
    width: 200px; height: 150px;
    border-radius: 50%;
    background: radial-gradient(ellipse at center, var(--emboss-light) 0%, var(--emboss) 60%, var(--back-dark) 100%);
  }
  .broker {
    position: absolute;
    left: 0; right: 0;
    top: 198px;
    text-align: center;
    font-family: "Cinzel", Georgia, serif;
    color: var(--emboss);
    text-shadow: 0 1px 0 rgba(255,255,255,0.12);
  }
  .broker-name { font-size: 28px; letter-spacing: 3px; line-height: 1; }
  .broker-sub { font-size: 12px; letter-spacing: 3px; margin-top: 4px; }
  .badges {
    position: absolute;
    right: 24px; bottom: 22px;
    display: flex; gap: 6px; align-items: center;
  }
  .badge { border: 1.5px solid var(--badge-white); }
  .badge-house { width: 24px; height: 24px; }
  .badge-realtor { width: 22px; height: 24px; }
  .badge-listing { width: 40px; height: 20px; background: var(--badge-white); }
</style>
</head>
<body>
  <section class="card card-front">
    <svg class="front-art" viewBox="0 0 540 309" aria-hidden="true">
      <path d="M0,300 C200,300 380,262 540,178 L540,309 L0,309 Z" fill="var(--brand-red)"/>
    </svg>
    <div role="img" aria-label="Black and white portrait photo of the realtor" style="position:absolute;left:340px;top:22px;width:200px;height:210px;background:linear-gradient(180deg,#d9d9d9 0%,#8a8a8a 55%,#2e2e2e 100%);"></div>
    <svg class="front-art" viewBox="0 0 540 309" aria-hidden="true">
      <path d="M0,309 L0,300 C200,300 380,262 540,178 L540,309 Z" fill="var(--brand-red)"/>
      <path d="M0,292 C210,292 390,248 540,164 L540,176 C380,258 200,288 0,288 Z" fill="var(--card-white)"/>
      <path d="M0,283 C215,285 395,240 540,158" fill="none" stroke="var(--line-gray)" stroke-width="5"/>
    </svg>

    <div class="brand-mark">
      <span class="brand-square"></span>
      <div>
        <div class="brand-name">LORENA WHITFIELD</div>
        <div class="brand-sub">REAL ESTATE</div>
      </div>
    </div>

    <div class="agent">
      <div class="agent-name">LORENA WHITFIELD</div>
      <div class="agent-title">Realtor</div>
    </div>

    <ul class="contact">
      <li>
        <svg viewBox="0 0 24 24"><path d="M6.6 10.8a15 15 0 0 0 6.6 6.6l2.2-2.2a1 1 0 0 1 1-.25 11.4 11.4 0 0 0 3.6.57 1 1 0 0 1 1 1V20a1 1 0 0 1-1 1A17 17 0 0 1 3 4a1 1 0 0 1 1-1h3.5a1 1 0 0 1 1 1c0 1.25.2 2.45.57 3.57a1 1 0 0 1-.25 1z"/></svg>
        480-555-0137
      </li>
      <li>
        <svg viewBox="0 0 24 24"><path d="M2 5h20v14H2z M2 5l10 8 10-8" /></svg>
        Lorena@LorenaWhitfieldRE.com
      </li>
    </ul>
  </section>

  <section class="card card-back">
    <div class="crest-ornament" role="img" aria-label="Embossed broker crest ornament"></div>
    <div class="broker">
      <div class="broker-name">HALDEN CREST</div>
      <div class="broker-sub">REAL ESTATE</div>
    </div>
    <div class="badges">
      <span class="badge badge-house"></span>
      <span class="badge badge-realtor"></span>
      <span class="badge badge-listing"></span>
    </div>
  </section>
</body>
</html>
```